Stickers signage for the outside of a 24 foot box truck.

This truck is for an oil field service truck, I have included a picture of the truck and the logo. The service is steam, heating and pressure washing for the oil field. Because of the large area to use for branding and advertising, I would like to have large decals placed on the truck, but not a full wrap due to the cost and the style is not what we are looking for.

I would like a series of large decals with log, phone number, email and some of the words mentioned, steam, heating, pressure washing place on. I would like some creativity in using the logo and graphics that compliment the logo. We are looking for edgy, and simplistic at the same time. Many truck wraps have so many things going on, the brand is lost. I have posted as well as example of a brand well recognized in the industry. Though I am not personally a fan of the truck design, it is well recognized instantly, and repeatable on each truck.

Given the name of the company Falcon Ridge, this gives the designer some leeway in using that in the design.

Sides, front, and back all available for signage.

Please only submit one design, unless the designs are completely different. I am looking for unique designs from different designers, and on one task done here, there were numerous similar designs submitted. Thank you for your submissions, all your hard work is appreciated.

There is a company called Teal Oilfield Services, they have a brand, recognizable and memorable. Very well designed. Also the task is now guaranteed.

0192cc
000000
ffffff

```html
<!DOCTYPE html>
<html lang="en">
<head>
<meta charset="utf-8">
<title>Falcon Ridge – Box Truck Decal Layouts</title>
<link href="https://fonts.googleapis.com/css2?family=Orbitron:wght@700;900&family=Roboto:wght@300;400;500&display=swap" rel="stylesheet">
<style>
  :root{
    --brand-blue:#0192cc;
    --ink:#000000;
    --paper:#ffffff;
    --stage:#e6e9ec;
    --frame:#1e1e1e;
  }
  *{box-sizing:border-box;margin:0;padding:0}
  html,body{width:1200px;height:946px;overflow:hidden}
  body{background:var(--stage);position:relative;font-family:"Roboto",Arial,sans-serif}

  .decal{position:absolute;left:120px;width:960px;height:400px;background:var(--paper);overflow:hidden;box-shadow:0 2px 8px rgba(0,0,0,.15)}
  .decal--band{top:40px}
  .decal--stripe{top:506px}

  .service-list{position:absolute;list-style:none}
  .service-list li{display:flex;align-items:center;gap:12px;font-size:19px;letter-spacing:1px;color:var(--ink);height:38px}
  .service-list .bullet{width:18px;height:18px;background:var(--brand-blue);display:inline-block}
  .decal--stripe .service-list .bullet{background:var(--paper);border:2px solid var(--brand-blue)}

  .door-frame{position:absolute;border:4px solid var(--frame);border-bottom:none}

  .brand{position:absolute;text-align:center}
  .brand-mark{width:80px;height:80px;background:var(--brand-blue)}
  .brand-name{font-family:"Orbitron",Arial,sans-serif;font-weight:900;font-size:54px;letter-spacing:2px;color:var(--ink);line-height:1;white-space:nowrap}
  .brand-tagline{font-family:"Orbitron",Arial,sans-serif;font-weight:700;font-size:18px;letter-spacing:9px;color:var(--brand-blue);margin-top:10px;white-space:nowrap}

  .contact-bar{position:absolute;left:0;right:0;bottom:0;display:flex;align-items:center;color:var(--paper)}
  .address{font-size:17px;line-height:1.25;white-space:nowrap}
  .phone{display:flex;align-items:center;gap:10px;font-size:42px;font-weight:300;letter-spacing:2px;white-space:nowrap}
  .phone svg{width:26px;height:36px}
  .online{font-size:14px;line-height:1.5;margin-left:auto;white-space:nowrap}
  .online span{display:flex;align-items:center;gap:6px}
  .online svg{width:14px;height:14px;flex:none}

  /* layout one: white panel with blue contact band */
  .decal--band .service-list{left:22px;top:100px}
  .decal--band .door-frame{left:178px;top:104px;width:160px;height:240px}
  .decal--band .brand-mark{position:absolute;left:610px;top:62px}
  .decal--band .brand{left:400px;width:500px;top:170px}
  .decal--band .contact-bar{height:56px;background:var(--brand-blue);padding:0 20px}
  .decal--band .address{width:340px}
  .decal--band .phone{padding-left:20px}

  /* layout two: blue stripe with black contact band */
  .stripe{position:absolute;left:0;right:0;background:var(--brand-blue)}
  .stripe--top{top:72px;height:54px}
  .stripe--bottom{top:252px;height:60px}
  .stripe--window{top:126px;height:126px;left:370px;right:0;background:var(--paper)}
  .decal--stripe .service-list{left:22px;top:128px}
  .decal--stripe .service-list li{height:31px;font-size:18px}
  .decal--stripe .door-frame{left:200px;top:52px;width:155px;height:260px}
  .decal--stripe .brand{left:375px;top:146px;display:flex;align-items:center;gap:18px;text-align:left}
  .decal--stripe .brand-mark{width:78px;height:78px}
  .decal--stripe .brand-name{font-size:50px}
  .decal--stripe .brand-tagline{font-size:16px;letter-spacing:8px}
  .decal--stripe .contact-bar{height:88px;background:var(--ink);padding:0 24px 0 30px}
  .decal--stripe .address{width:340px}
</style>
</head>
<body>

<section class="decal decal--band" aria-label="Side decal layout one">
  <ul class="service-list">
    <li><span class="bullet"></span>SERVICE</li>
    <li><span class="bullet"></span>SERVICE</li>
    <li><span class="bullet"></span>SERVICE</li>
    <li><span class="bullet"></span>SERVICE</li>
  </ul>
  <div class="brand-mark"></div>
  <div class="brand">
    <div class="brand-name">FALCON RIDGE</div>
    <div class="brand-tagline">OILFIELD SERVICES LIMITED</div>
  </div>
  <div class="door-frame"></div>
  <div class="contact-bar">
    <div class="address">address address address<br>address address address</div>
    <div class="phone">
      <svg viewBox="0 0 26 36"><rect x="4" y="2" width="18" height="32" rx="4" fill="none" stroke="#fff" stroke-width="3"/><rect x="9" y="28" width="8" height="2" fill="#fff"/></svg>
      0555 014 278
    </div>
    <div class="online">
      <span><svg viewBox="0 0 14 14"><circle cx="7" cy="7" r="6" fill="none" stroke="#fff" stroke-width="1.5"/><path d="M1 7h12M7 1c3 3 3 9 0 12M7 1c-3 3-3 9 0 12" fill="none" stroke="#fff" stroke-width="1"/></svg>www.falconridge-oil.com</span>
      <span><svg viewBox="0 0 14 14"><rect x="1" y="3" width="12" height="8" fill="none" stroke="#fff" stroke-width="1.5"/><path d="M1 3l6 5 6-5" fill="none" stroke="#fff" stroke-width="1.2"/></svg>info@falconridge-oil.com</span>
    </div>
  </div>
</section>

<section class="decal decal--stripe" aria-label="Side decal layout two">
  <div class="stripe stripe--top"></div>
  <div class="stripe stripe--bottom"></div>
  <div class="stripe stripe--window"></div>
  <ul class="service-list">
    <li><span class="bullet"></span>SERVICE</li>
    <li><span class="bullet"></span>SERVICE</li>
    <li><span class="bullet"></span>SERVICE</li>
    <li><span class="bullet"></span>SERVICE</li>
  </ul>
  <div class="brand">
    <div class="brand-mark"></div>
    <div>
      <div class="brand-name">FALCON RIDGE</div>
      <div class="brand-tagline">OILFIELD SERVICES LIMITED</div>
    </div>
  </div>
  <div class="door-frame"></div>
  <div class="contact-bar">
    <div class="address">address address address<br>address address address</div>
    <div class="phone">
      <svg viewBox="0 0 26 36"><rect x="4" y="2" width="18" height="32" rx="4" fill="none" stroke="#fff" stroke-width="3"/><rect x="9" y="28" width="8" height="2" fill="#fff"/></svg>
      0555 014 278
    </div>
    <div class="online">
      <span><svg viewBox="0 0 14 14"><circle cx="7" cy="7" r="6" fill="none" stroke="#fff" stroke-width="1.5"/><path d="M1 7h12M7 1c3 3 3 9 0 12M7 1c-3 3-3 9 0 12" fill="none" stroke="#fff" stroke-width="1"/></svg>www.falconridge-oil.com</span>
      <span><svg viewBox="0 0 14 14"><rect x="1" y="3" width="12" height="8" fill="none" stroke="#fff" stroke-width="1.5"/><path d="M1 3l6 5 6-5" fill="none" stroke="#fff" stroke-width="1.2"/></svg>info@falconridge-oil.com</span>
    </div>
  </div>
</section>

</body>
</html>
```